"Velmaro" sparkling beverage

Dear All!
I need a stick label (82*95 - front label, 82*65 - back label )design for а sparkling beverage, name is "Velmaro", 4 flavours: lemonade,duchess pear, estragon, original. Transparent glass bottles 0,5 liter (alumnium closure 28*15)/0,33 liter (crown cap), neck label should also be on the bottle 0,5 liter.
European style is welcomed
Do not send the disigns with a little changes several times, please!!!
Young people from 12-30 ages old

```html
<!DOCTYPE html>
<html lang="en">
<head>
<meta charset="utf-8">
<title>Velmaro Estragon – Labels</title>
<link rel="stylesheet" href="https://fonts.googleapis.com/css2?family=Oswald:wght@400;500&display=swap">
<style>
  :root {
    --bg: #ffffff;
    --green-deep: #17612a;
    --green-mid: #2f8a3c;
    --green-soft: #4f9e52;
    --ink-light: #ffffff;
    --ink-muted: #e4f1e2;
  }
  * { margin: 0; padding: 0; box-sizing: border-box; }
  html, body {
    width: 1200px; height: 998px; overflow: hidden;
    background: var(--bg);
    font-family: "Oswald", "Arial Narrow", sans-serif;
  }
  .canvas { position: relative; width: 1200px; height: 998px; }

  .neck-label {
    position: absolute; left: 390px; top: 40px;
    width: 420px; height: 170px;
  }
  .neck-label svg, .front-label svg { position: absolute; inset: 0; }
  .neck-label .brand-name {
    position: absolute; inset: 0;
    display: flex; align-items: center; justify-content: center;
    font-size: 54px; font-weight: 500; color: var(--ink-light);
    letter-spacing: 1px;
  }

  .front-label {
    position: absolute; left: 290px; top: 250px;
    width: 620px; height: 700px;
  }
  .front-content {
    position: absolute; inset: 0;
    display: flex; flex-direction: column; align-items: center;
    color: var(--ink-light); text-align: center;
  }
  .front-content .brand-name {
    margin-top: 150px;
    font-size: 96px; font-weight: 500; line-height: 1; letter-spacing: 2px;
  }
  .tagline {
    margin-top: 34px;
    font-size: 38px; font-weight: 400; line-height: 1; letter-spacing: 0.5px;
  }
  .flavour {
    margin-top: 10px;
    font-size: 58px; font-weight: 500; line-height: 1; letter-spacing: 1px;
  }
  .ingredients {
    margin-top: 30px; width: 470px;
    font-size: 12px; font-weight: 400; line-height: 1.45;
    color: var(--ink-muted); text-align: justify;
  }
  .volume {
    margin-top: 62px;
    font-size: 22px; font-weight: 500; letter-spacing: 0.5px;
  }
</style>
</head>
<body>
<main class="canvas">

  <section class="neck-label" aria-label="Neck label">
    <svg width="420" height="170" viewBox="0 0 420 170" aria-hidden="true">
      <path d="M0,30 Q210,-10 420,30 L420,140 Q210,180 0,140 Z" fill="var(--green-deep)"/>
    </svg>
    <div class="brand-name">Velmaro</div>
  </section>

  <section class="front-label" aria-label="Front label">
    <svg width="620" height="700" viewBox="0 0 620 700" aria-hidden="true">
      <rect x="0" y="90" width="620" height="520" fill="var(--green-soft)"/>
      <path d="M40,80 Q310,-10 580,80 L580,610 Q310,720 40,610 Z" fill="var(--green-mid)"/>
      <path d="M40,560 L580,560 L580,610 Q310,720 40,610 Z" fill="var(--green-deep)"/>
    </svg>
    <div class="front-content">
      <div class="brand-name">Velmaro</div>
      <div class="tagline">PREMIUM BEVERAGE</div>
      <div class="flavour">ESTRAGON</div>
      <p class="ingredients">Sparkling water, sugar, natural tarragon extract, citric acid, carbon dioxide. Best served chilled. Shake gently before opening and enjoy with friends. Store in a cool dry place away from direct sunlight. Recycle the glass bottle after use.</p>
      <div class="volume">0,5 LITER</div>
    </div>
  </section>

</main>
</body>
</html>
```